Mortgage Map Flyer / Email Design

To create a one page document / email that shows a map / road map of the Mortgage Process

Client decides to Purchase a Home
Client find a reputable lenders, typically online or through a trusted friend / resource
Sets an appointment to either meet with that Lender / Loan officer in person, or speaks on the phone
Review credit and borrower documents
Pre Qualification so we stay within the budget of the client or a plan is put in place to help borrower qualify for the purchase they are seeking
Find a trust Realtor to search for homes
Tour homes to find the right fit for the client and their family
Make an offer
Ratify the contract & sign loan disclosures
Go into underwriting
Loan Approval
Sign final loan documents
Fund and move in!

Target Market(s)

Clients looking to purchase a home

Industry/Entity Type

Mortgage

Font styles to use
Sans Serif

Requirements
Must have
• Pictures, road map or map with arrows pointing the way through the process. Want to have something I can print, or embed in an email
Nice to have
• Looking to have similar colors and feel as our branch website, with our loan process videos at www.rlkhome.example
• Our logo and colors would be obviously nice to tie in as well!

```html
<!DOCTYPE html>
<html lang="en">
<head>
<meta charset="utf-8">
<title>Ridgelake Bank – Mortgage Road Map</title>
<link href="https://fonts.googleapis.com/css2?family=Lato:wght@300;400&display=swap" rel="stylesheet">
<style>
  :root {
    --ink: #2f2f31;
    --tile: #3a3a3c;
    --gold: #f2c26e;
    --paper: #ffffff;
    --panel: #e8e9eb;
    --text: #3b3b3d;
    --light: #f4f2ee;
    --sofa: #c79a5e;
    --box: #b98e5c;
    --shirt: #a9d8bf;
  }
  * { box-sizing: border-box; margin: 0; padding: 0; }
  html, body { width: 1014px; height: 1200px; overflow: hidden; background: var(--panel); }
  body { font-family: "Lato", Arial, sans-serif; color: var(--text); }
  .flyer { position: relative; width: 1014px; height: 1200px; background: var(--panel); }

  .masthead { position: absolute; left: 0; top: 0; width: 100%; height: 116px; background: var(--paper); }
  .brand { position: absolute; left: 47px; top: 24px; display: flex; align-items: center; gap: 26px; }
  .brand-square { width: 84px; height: 78px; background: var(--ink); }
  .brand-name { font-weight: 300; font-size: 33px; letter-spacing: 3px; text-transform: uppercase; color: var(--ink); }
  .tagline { position: absolute; right: 50px; top: 38px; font-size: 32px; font-weight: 400; color: var(--gold); }

  .hero { position: absolute; left: 0; top: 116px; width: 100%; height: 560px; }
  .hero-photo {
    position: absolute; inset: 0;
    background:
      radial-gradient(ellipse 120px 170px at 600px 230px, rgba(169,216,191,.75), rgba(169,216,191,0) 100%),
      radial-gradient(ellipse 130px 150px at 420px 290px, rgba(255,255,255,.8), rgba(255,255,255,0) 100%),
      radial-gradient(ellipse 110px 120px at 690px 430px, rgba(240,244,250,.85), rgba(240,244,250,0) 100%),
      radial-gradient(ellipse 220px 110px at 470px 480px, rgba(185,142,92,.7), rgba(185,142,92,0) 100%),
      linear-gradient(180deg, var(--light) 0%, #ece6dc 30%, #d9b98a 52%, var(--sofa) 72%, var(--box) 100%);
  }
  .hero-curve { position: absolute; left: 0; top: 0; width: 100%; height: 560px; }

  .step { position: absolute; display: flex; align-items: center; gap: 15px; }
  .step-icon { flex: none; width: 52px; height: 52px; background: var(--tile); border-radius: 3px; display: flex; align-items: center; justify-content: center; }
  .step-icon svg { width: 32px; height: 32px; }
  .step-text { font-size: 16.5px; line-height: 1.13; font-weight: 400; }
  .col-left { left: 33px; width: 468px; }
  .col-left .step-text { width: 401px; }
  .col-right { left: 556px; width: 430px; }
  .col-right .step-text { width: 355px; }
  .justify { text-align: justify; }

  .footer { position: absolute; left: 0; bottom: 0; width: 100%; height: 62px; background: var(--tile); display: flex; align-items: center; justify-content: center; }
  .footer-url { color: var(--gold); font-size: 26px; letter-spacing: 6px; font-weight: 400; }
</style>
</head>
<body>
<div class="flyer">
  <header class="masthead">
    <div class="brand">
      <div class="brand-square"></div>
      <div class="brand-name">Ridgelake Bank</div>
    </div>
    <div class="tagline">Mortages Made Simple!</div>
  </header>

  <section class="hero">
    <div class="hero-photo" role="img" aria-label="Photo of a smiling family of four unpacking moving boxes on a tan sofa in a bright new home"></div>
    <svg class="hero-curve" viewBox="0 0 1014 560" preserveAspectRatio="none" aria-hidden="true">
      <path d="M0 414 Q507 670 1014 404 L1014 560 L0 560 Z" fill="#e8e9eb"/>
      <path d="M0 414 Q507 670 1014 404" fill="none" stroke="#f2c26e" stroke-width="7"/>
    </svg>
  </section>

  <section class="steps">
    <div class="step col-left" style="top:710px">
      <div class="step-icon"><svg viewBox="0 0 32 32"><path d="M16 5 L3 17 H7 V28 H13 V20 H19 V28 H25 V17 H29 Z" fill="#f2c26e"/></svg></div>
      <div class="step-text">Client decides to Purchase a Home</div>
    </div>
    <div class="step col-left" style="top:775px">
      <div class="step-icon"><svg viewBox="0 0 32 32"><circle cx="13" cy="13" r="8" fill="none" stroke="#f2c26e" stroke-width="3"/><path d="M19 19 L28 28" stroke="#f2c26e" stroke-width="4" stroke-linecap="round"/></svg></div>
      <div class="step-text">Client find a reputable lenders, typically online or through a trusted friend / resource</div>
    </div>
    <div class="step col-left" style="top:845px">
      <div class="step-icon"><svg viewBox="0 0 32 32"><rect x="5" y="7" width="22" height="21" rx="2" fill="none" stroke="#f2c26e" stroke-width="2.5"/><path d="M5 12 H27 M10 4 V9 M22 4 V9" stroke="#f2c26e" stroke-width="2.5"/><path d="M11 20 L15 24 L22 16" fill="none" stroke="#f2c26e" stroke-width="2.5"/></svg></div>
      <div class="step-text justify">Sets an appointment to either meet with that Lender / Loan officer in person, or speaks on the phone</div>
    </div>
    <div class="step col-left" style="top:913px">
      <div class="step-icon"><svg viewBox="0 0 32 32"><rect x="8" y="4" width="17" height="24" rx="1" fill="none" stroke="#f2c26e" stroke-width="2.5"/><path d="M12 10 H21 M12 15 H21 M12 20 H21" stroke="#f2c26e" stroke-width="2"/></svg></div>
      <div class="step-text">Review credit and borrower documents</div>
    </div>
    <div class="step col-left" style="top:984px">
      <div class="step-icon"><svg viewBox="0 0 32 32"><rect x="4" y="5" width="22" height="16" fill="none" stroke="#f2c26e" stroke-width="2.5"/><path d="M8 10 H22 M8 15 H18" stroke="#f2c26e" stroke-width="2"/><circle cx="21" cy="23" r="4" fill="#f2c26e"/><path d="M19 26 L18 30 M23 26 L24 30" stroke="#f2c26e" stroke-width="2"/></svg></div>
      <div class="step-text">Pre Qualification so we stay within the budget of the client or a plan is put in place to help borrower qualify for the purchase they are seeking</div>
    </div>
    <div class="step col-left" style="top:1052px">
      <div class="step-icon"><svg viewBox="0 0 32 32"><path d="M14 4 L2 15 H6 V27 H22 V15 H26 Z" fill="#f2c26e"/><circle cx="20" cy="17" r="4" fill="#3a3a3c"/><path d="M13 29 Q20 19 27 29 Z" fill="#3a3a3c"/></svg></div>
      <div class="step-text">Find a trust Realtor to search for homes</div>
    </div>

    <div class="step col-right" style="top:709px">
      <div class="step-icon"><svg viewBox="0 0 32 32"><path d="M14 4 L3 14 H6 V27 H22 V14 H25 Z" fill="#f2c26e"/><circle cx="15" cy="17" r="5" fill="#3a3a3c"/><path d="M18 20 L27 29" stroke="#f2c26e" stroke-width="3.5" stroke-linecap="round"/></svg></div>
      <div class="step-text">Tour homes to find the right fit for the client and their family</div>
    </div>
    <div class="step col-right" style="top:781px">
      <div class="step-icon"><svg viewBox="0 0 32 32"><path d="M16 4 L3 15 H7 V28 H25 V15 H29 Z" fill="#f2c26e"/><circle cx="16" cy="20" r="5" fill="#3a3a3c"/><text x="16" y="23.5" font-size="9" text-anchor="middle" fill="#f2c26e" font-family="Arial, sans-serif">$</text></svg></div>
      <div class="step-text">Make an offer</div>
    </div>
    <div class="step col-right" style="top:846px">
      <div class="step-icon"><svg viewBox="0 0 32 32"><rect x="5" y="7" width="18" height="21" fill="none" stroke="#f2c26e" stroke-width="2.5"/><path d="M13 20 L26 6 L29 9 L16 23 L12 24 Z" fill="#f2c26e"/></svg></div>
      <div class="step-text">Ratify the contract &amp; sign loan disclosures<br>Go into underwriting</div>
    </div>
    <div class="step col-right" style="top:915px">
      <div class="step-icon"><svg viewBox="0 0 32 32"><circle cx="16" cy="7" r="4" fill="#f2c26e"/><rect x="13" y="10" width="6" height="9" fill="#f2c26e"/><rect x="6" y="19" width="20" height="5" rx="1" fill="#f2c26e"/><rect x="6" y="26" width="20" height="2" fill="#f2c26e"/></svg></div>
      <div class="step-text">Loan Approval</div>
    </div>
    <div class="step col-right" style="top:986px">
      <div class="step-icon"><svg viewBox="0 0 32 32"><rect x="6" y="4" width="20" height="24" fill="#f2c26e"/><rect x="12" y="4" width="2" height="24" fill="#3a3a3c"/><path d="M18 4 V13 L20.5 11 L23 13 V4 Z" fill="#3a3a3c"/></svg></div>
      <div class="step-text">Sign final loan documents</div>
    </div>
    <div class="step col-right" style="top:1054px">
      <div class="step-icon"><svg viewBox="0 0 32 32"><path d="M16 3 L5 13 H8 V21 H24 V13 H27 Z" fill="#f2c26e"/><rect x="14" y="15" width="4" height="6" fill="#3a3a3c"/><path d="M3 19 Q6 29 16 29 Q26 29 29 19" fill="none" stroke="#f2c26e" stroke-width="3"/></svg></div>
      <div class="step-text">Fund and move in!</div>
    </div>
  </section>

  <footer class="footer">
    <div class="footer-url">www.rlkhome.example</div>
  </footer>
</div>
</body>
</html>
```